Onsite Energy for Retail Tenants

Need a short one page-3 part build showing how the program for discounted clean energy works - moving into a call to action with multiple links.

1) Solar Garden Produces Energy
2) Credits Available for Tenants’ Utility Bills
3) Sign Up to Receive Utility Bill Credits.
Save 5%

This document will be used:
1) Embedded in Mailchimp emails
2) as an html landing page
3) as an image

Use the latest powerpoint Tenant slide E as guidance

Infographic is simplistic. 3 part build using graphics and information. Flow is really important so Gifs welcome.

Target Market(s)

Owners of small stores throughout the US.

Industry/Entity Type

Real Estate

Colors

Designer to choose colors to be used in the design.

Requirements
Must have
• It must explain the program clearly and succinctly using the language from the first slide of Mockup 1. This slide must become an elegant build for the 3 step process. See Mockup 2 for its cleanliness ideas for a similar but different program.
• The second slide of mockup 1 is the call to action and must have clickable links and promote trust.
• Please use the attached font styles.
• The text is sparse and so needs to be bold and in order and with the graphics needs to explain how it works perfectly.
• The graphics should be clean and sophisticated but the message and flow needs to be simple.
Nice to have
• Moving arrows to show flow of energy and credits.
• Ability to switch out language of text.

```html
<!DOCTYPE html>
<html lang="en">
<head>
<meta charset="utf-8">
<title>Brightfield – Local Discount Energy Program</title>
<link rel="stylesheet" href="https://fonts.googleapis.com/css2?family=Open+Sans:wght@400;600;700;800&display=swap">
<style>
  :root {
    --orange: #e8692a;
    --orange-deep: #d85a1e;
    --ink: #231f20;
    --sky: #cfe9f6;
    --sky-soft: #e6f4fb;
    --white: #ffffff;
  }
  * { margin: 0; padding: 0; box-sizing: border-box; }
  html, body { width: 1200px; height: 3000px; overflow: hidden; background: var(--white); }
  body { font-family: "Open Sans", Arial, sans-serif; position: relative; }

  .brand {
    position: absolute; left: 80px; top: 60px;
    display: flex; align-items: center; gap: 16px;
  }
  .brand-dot { width: 46px; height: 46px; border-radius: 50%; background: var(--orange); }
  .brand-name { font-weight: 800; font-size: 64px; color: var(--ink); letter-spacing: -1px; line-height: 1; }

  .program-title {
    position: absolute; left: 76px; top: 222px;
    color: var(--orange); font-weight: 700; font-size: 52px; line-height: 66px;
  }

  .flow { position: absolute; left: 0; top: 0; width: 1200px; height: 2556px; }
  .flow text { font-family: "Open Sans", Arial, sans-serif; fill: var(--white); text-anchor: middle; }
  .step-number { font-weight: 800; font-size: 46px; }
  .step-text { font-weight: 700; font-size: 22px; }

  .cta-band {
    position: absolute; left: 0; top: 2556px; width: 1200px; height: 100px;
    background: var(--orange); color: var(--white);
    font-weight: 600; font-size: 38px; line-height: 100px; padding-left: 80px;
  }
  .benefits-band {
    position: absolute; left: 0; top: 2656px; width: 1200px; height: 244px;
    background: var(--ink);
  }
  .benefit-list {
    position: absolute; left: 136px; top: 26px; list-style: none;
    color: var(--white); font-weight: 600; font-size: 28px; line-height: 37px;
  }
  .benefit-list li::before { content: "• "; }
  .contact-button {
    position: absolute; left: 900px; top: 44px; width: 160px; height: 160px;
    border-radius: 50%; background: var(--orange); color: var(--white);
    text-decoration: none; text-align: center;
    display: flex; flex-direction: column; align-items: center; justify-content: center;
    font-weight: 700; font-size: 25px; line-height: 32px;
  }
  .contact-button svg { width: 26px; height: 26px; margin-bottom: 4px; }

  .estimate-band {
    position: absolute; left: 0; top: 2900px; width: 1200px; height: 100px;
    background: var(--orange); color: var(--white);
  }
  .partner-name {
    position: absolute; left: 116px; top: 26px;
    font-weight: 700; font-size: 40px; line-height: 48px; letter-spacing: 1px;
  }
  .band-divider { position: absolute; left: 364px; top: 22px; width: 2px; height: 56px; background: var(--white); }
  .estimate-link {
    position: absolute; left: 384px; top: 16px; color: var(--white); text-decoration: none;
  }
  .estimate-title { display: block; font-weight: 700; font-size: 29px; line-height: 38px; }
  .estimate-note { display: block; font-weight: 400; font-size: 16px; line-height: 22px; }
</style>
</head>
<body>

  <div class="brand">
    <span class="brand-dot"></span>
    <span class="brand-name">Brightfield</span>
  </div>

  <h1 class="program-title">Local<br>Discount<br>Energy<br>Program</h1>

  <svg class="flow" viewBox="0 0 1200 2556" xmlns="http://www.w3.org/2000/svg">
    <defs>
      <linearGradient id="sky-fill" x1="0" y1="0" x2="0" y2="1">
        <stop offset="0" stop-color="#d6eefa"/>
        <stop offset="0.6" stop-color="#bfe2f4"/>
        <stop offset="1" stop-color="#f08a52"/>
      </linearGradient>
    </defs>

    <!-- connector -->
    <line x1="580" y1="544" x2="580" y2="2240" stroke="var(--orange)" stroke-width="6" stroke-dasharray="8 8"/>

    <!-- scene circles -->
    <g role="img" aria-label="Illustration of a solar-powered storefront with shoppers under the sun">
      <circle cx="580" cy="370" r="170" fill="url(#sky-fill)" stroke="var(--orange)" stroke-width="8"/>
    </g>
    <g role="img" aria-label="Illustration of utility poles and power lines carrying energy">
      <circle cx="580" cy="1140" r="170" fill="url(#sky-fill)" stroke="var(--orange)" stroke-width="8"/>
    </g>
    <g role="img" aria-label="Illustration of a store tenant waving from a shop window">
      <circle cx="580" cy="1970" r="170" fill="url(#sky-fill)" stroke="var(--orange)" stroke-width="8"/>
    </g>

    <!-- flow markers -->
    <g class="marker">
      <path d="M548 562 H612 L580 606 Z" fill="var(--orange)"/>
      <path d="M584 568 L572 584 H581 L576 598 L590 580 H581 Z" fill="var(--white)"/>
    </g>
    <g class="marker">
      <path d="M548 922 H612 L580 966 Z" fill="var(--orange)"/>
      <path d="M584 928 L572 944 H581 L576 958 L590 940 H581 Z" fill="var(--white)"/>
    </g>
    <g class="marker">
      <path d="M548 1368 H612 L580 1412 Z" fill="var(--orange)"/>
      <text x="580" y="1394" style="font-size:22px;font-weight:800">$</text>
    </g>
    <g class="marker">
      <path d="M548 1732 H612 L580 1776 Z" fill="var(--orange)"/>
      <text x="580" y="1758" style="font-size:22px;font-weight:800">$</text>
    </g>
    <g class="marker">
      <path d="M548 2198 H612 L580 2242 Z" fill="var(--orange)"/>
      <path d="M572 2206 H588 L580 2222 Z" fill="var(--white)"/>
    </g>

    <!-- steps -->
    <g class="step">
      <circle cx="580" cy="750" r="130" fill="var(--orange)"/>
      <text class="step-number" x="580" y="705">1</text>
      <text class="step-text" x="580" y="748">Solar Garden</text>
      <text class="step-text" x="580" y="776">Produces Energy</text>
      <text class="step-text" x="580" y="804">which becomes</text>
      <text class="step-text" x="580" y="832">Utility Credits</text>
    </g>
    <g class="step">
      <circle cx="580" cy="1570" r="130" fill="var(--orange)"/>
      <text class="step-number" x="580" y="1525">2</text>
      <text class="step-text" x="580" y="1568">Credits Available</text>
      <text class="step-text" x="580" y="1596">for the property's</text>
      <text class="step-text" x="580" y="1624">Tenants'</text>
      <text class="step-text" x="580" y="1652">Utility Bills</text>
    </g>
    <g class="step">
      <circle cx="580" cy="2370" r="130" fill="var(--orange)"/>
      <text class="step-number" x="580" y="2325">3</text>
      <text class="step-text" x="580" y="2368">Sign Up to</text>
      <text class="step-text" x="580" y="2396">Receive</text>
      <text class="step-text" x="580" y="2424">Utility Bill</text>
      <text class="step-text" x="580" y="2452">Credits</text>
    </g>
  </svg>

  <div class="cta-band">Sign Up now for the Energy Discount Subscription</div>

  <div class="benefits-band">
    <ul class="benefit-list">
      <li>No Cost</li>
      <li>No change to current Utility Power</li>
      <li>5% Discount off Utility Price Guaranteed</li>
      <li>For as long as you lease the store</li>
      <li>Optional “Brightfield” Store decal</li>
    </ul>
    <a class="contact-button" href="#contact">
      <svg viewBox="0 0 24 24" aria-hidden="true"><path fill="#fff" d="M6.6 10.8a15.1 15.1 0 0 0 6.6 6.6l2.2-2.2c.3-.3.7-.4 1-.2 1.1.4 2.3.6 3.6.6.6 0 1 .4 1 1V20c0 .6-.4 1-1 1A17 17 0 0 1 3 4c0-.6.4-1 1-1h3.5c.6 0 1 .4 1 1 0 1.3.2 2.5.6 3.6.1.3 0 .7-.2 1z"/></svg>
      Contact<br>Us
    </a>
  </div>

  <div class="estimate-band">
    <span class="partner-name">MeterLink</span>
    <span class="band-divider"></span>
    <a class="estimate-link" href="#estimate">
      <span class="estimate-title">Get an Estimate of How Much You Will Save</span>
      <span class="estimate-note">Online Utility Account required for this step • Energy Data Never Sold or Distributed</span>
    </a>
  </div>

</body>
</html>
```